Sheriff Candidate needs a large yard sign

A candidate for Sheriff needs to have a sign to put in front of businesses and houses that advertise her candidacy.

Target Market(s)

Democrats, voters

Industry/Entity Type

Political

Font styles to use
Sans Serif

Colors
34a7d7
3276b5

Requirements
Must have
• Must have her picture
• Must have the words "Elect Dana Whitlock" - I'd like the name Dana to be smaller Whitlock. "Elect" and "Whitlock" should be the focus.
• at the bottom in a box "Paid for by the Committee to Elect Dana Whitlock"
Nice to have
• it would be good to have her logo as well.
• blue color for democrats and on a white background
Should not have
• pink color

```html
<!DOCTYPE html>
<html lang="en">
<head>
<meta charset="utf-8">
<title>Elect Dana Whitlock – Yard Sign</title>
<link rel="stylesheet" href="https://fonts.googleapis.com/css2?family=Anton&family=Krona+One&family=Source+Sans+3:wght@400;500&display=swap">
<style>
  :root {
    --sky-blue: #34a7d7;
    --deep-blue: #3276b5;
    --stripe-grey: #c9c9c9;
    --backdrop-dark: #55504f;
    --backdrop-light: #8b8685;
    --blazer-navy: #1c2233;
    --white: #ffffff;
    --ink: #111111;
    --gold: #c9a43a;
  }
  * { margin: 0; padding: 0; box-sizing: border-box; }
  html, body {
    width: 932px;
    height: 1200px;
    overflow: hidden;
    background: var(--white);
  }
  .yard-sign {
    position: relative;
    width: 932px;
    height: 1200px;
    overflow: hidden;
    background: var(--deep-blue);
  }
  .sign-shapes {
    position: absolute;
    inset: 0;
    width: 932px;
    height: 1200px;
  }
  .candidate-portrait {
    position: absolute;
    inset: 0;
    clip-path: polygon(538px 0, 932px 0, 932px 1200px, 335px 1200px);
    background:
      radial-gradient(ellipse 330px 520px at 700px 1130px, var(--blazer-navy) 0%, var(--blazer-navy) 62%, rgba(28,34,51,0) 100%),
      radial-gradient(ellipse 120px 150px at 590px 590px, #b08670 0%, #8a6a5c 60%, rgba(138,106,92,0) 100%),
      radial-gradient(ellipse at 60% 40%, var(--backdrop-light) 0%, #6f6a69 45%, var(--backdrop-dark) 100%);
  }
  .headline {
    position: absolute;
    left: 78px;
    top: 84px;
    color: var(--white);
    text-shadow: 3px 3px 0 var(--ink);
    font-weight: 400;
  }
  .headline-elect {
    display: block;
    font-family: "Krona One", sans-serif;
    font-size: 112px;
    line-height: 1;
    letter-spacing: 10px;
  }
  .headline-name {
    display: flex;
    align-items: baseline;
    gap: 22px;
    margin-top: 14px;
    font-family: "Anton", sans-serif;
    line-height: 1;
    text-transform: uppercase;
  }
  .first-name { font-size: 98px; }
  .last-name { font-size: 128px; }
  .campaign-mark {
    position: absolute;
    left: 70px;
    top: 500px;
    width: 340px;
    display: flex;
    flex-direction: column;
    align-items: center;
    gap: 22px;
  }
  .campaign-mark-dot {
    width: 120px;
    height: 120px;
    border-radius: 50%;
    background: var(--gold);
  }
  .campaign-mark-name {
    font-family: "Source Sans 3", sans-serif;
    font-weight: 500;
    font-size: 34px;
    color: var(--white);
    text-transform: uppercase;
    text-align: center;
    line-height: 1.15;
  }
  .paid-for {
    position: absolute;
    left: 59px;
    top: 926px;
    color: var(--white);
    font-family: "Source Sans 3", sans-serif;
    text-transform: uppercase;
  }
  .paid-for-lead {
    display: block;
    font-size: 35px;
    font-weight: 400;
    line-height: 37px;
  }
  .paid-for-committee {
    display: block;
    font-size: 40px;
    font-weight: 500;
    line-height: 45px;
    margin-top: 6px;
  }
</style>
</head>
<body>
  <main class="yard-sign">
    <div class="candidate-portrait" role="img" aria-label="Portrait photo of candidate Dana Whitlock smiling, wearing a navy blazer, against a grey studio backdrop"></div>

    <svg class="sign-shapes" viewBox="0 0 932 1200" aria-hidden="true">
      <polygon class="divider-stripe" points="527,0 538,0 335,1200 280,1200" fill="var(--stripe-grey)"/>
      <polygon class="title-band" points="0,45 864,45 811,354 0,354" fill="var(--sky-blue)"/>
      <polygon class="corner-stripe" points="887,45 932,45 932,354 837,354" fill="var(--white)"/>
      <rect class="disclaimer-box" x="0" y="883" width="388" height="255" fill="var(--sky-blue)"/>
    </svg>

    <h1 class="headline">
      <span class="headline-elect">ELECT</span>
      <span class="headline-name">
        <span class="first-name">Dana</span>
        <span class="last-name">Whitlock</span>
      </span>
    </h1>

    <div class="campaign-mark">
      <span class="campaign-mark-dot"></span>
      <span class="campaign-mark-name">Whitlock for Sheriff<br>Democrat</span>
    </div>

    <p class="paid-for">
      <span class="paid-for-lead">Paid for by the</span>
      <span class="paid-for-lead">Committee</span>
      <span class="paid-for-committee">To Elect<br>Dana Whitlock</span>
    </p>
  </main>
</body>
</html>
```